KORVELTA Corporate Business Card

Modern business card design for company which focuses in the areas of Staffing, IT Consulting & Data Services. Please note: We are no longer using the IT subscript on the logo. All designs should have IT subscript removed.
Website: www.korveltait.example

```html
<!DOCTYPE html>
<html lang="en">
<head>
<meta charset="utf-8">
<title>KORVELTA Business Card</title>
<link href="https://fonts.googleapis.com/css2?family=Lato:wght@400;700&display=swap" rel="stylesheet">
<style>
  :root {
    --canvas-grey: #d6d6d6;
    --card-white: #ffffff;
    --brand-light: #1e9ad6;
    --brand-dark: #0a5892;
    --ink: #333333;
  }
  * { margin: 0; padding: 0; box-sizing: border-box; }
  html, body { width: 1000px; height: 1200px; overflow: hidden; }
  body {
    background: var(--canvas-grey);
    font-family: "Lato", sans-serif;
    position: relative;
  }
  .card {
    position: absolute;
    box-shadow: 6px 8px 22px rgba(0,0,0,0.45);
    overflow: hidden;
  }
  .card-front {
    left: 111px; top: 120px; width: 777px; height: 446px;
    background: var(--card-white);
  }
  .card-back {
    left: 109px; top: 633px; width: 782px; height: 447px;
    background: var(--brand-dark);
  }
  .brand {
    position: absolute;
    display: flex; align-items: center;
    color: var(--brand-light);
    font-weight: 700;
    letter-spacing: 1px;
    line-height: 1;
  }
  .brand-mark { background: var(--brand-light); flex: none; }
  .card-front .brand { left: 64px; top: 200px; font-size: 50px; }
  .card-front .brand-mark { width: 34px; height: 34px; margin-right: 14px; }
  .card-back .brand { left: 0; right: 0; justify-content: center; top: 188px; font-size: 92px; }
  .card-back .brand-mark { width: 62px; height: 62px; margin-right: 24px; }
  .divider {
    position: absolute; left: 393px; top: 124px;
    width: 2px; height: 199px; background: var(--brand-dark);
  }
  .contact-block { position: absolute; left: 432px; top: 118px; color: var(--ink); }
  .person-name { font-size: 24px; font-weight: 700; color: var(--brand-light); line-height: 30px; }
  .person-role { font-size: 19px; line-height: 26px; margin-bottom: 10px; }
  .address { font-size: 19px; line-height: 28px; margin-bottom: 8px; }
  .contact-line { display: flex; align-items: center; font-size: 19px; line-height: 28px; }
  .contact-line svg { width: 18px; height: 18px; margin-right: 9px; flex: none; }
  .footer-band { position: absolute; left: 0; bottom: 0; width: 777px; height: 48px; }
  .office-hours {
    position: absolute; left: 469px; bottom: 13px;
    color: var(--card-white); font-size: 19px;
  }
  .back-url {
    position: absolute; left: 0; right: 0; top: 390px;
    text-align: center; color: var(--card-white); font-size: 19px;
  }
</style>
</head>
<body>
  <section class="card card-front">
    <div class="brand"><span class="brand-mark"></span>KORVELTA</div>
    <div class="divider"></div>
    <div class="contact-block">
      <p class="person-name">DARREN HOLLOWAY</p>
      <p class="person-role">Owner</p>
      <p class="address">418 Harlow Ave, Brennfield<br>IN 47000, USA</p>
      <p class="contact-line">
        <svg viewBox="0 0 24 24"><path fill="#1e9ad6" d="M6.6 10.8a15.1 15.1 0 0 0 6.6 6.6l2.2-2.2c.3-.3.7-.4 1-.2 1.1.4 2.3.6 3.6.6.6 0 1 .4 1 1V20c0 .6-.4 1-1 1A17 17 0 0 1 3 4c0-.6.4-1 1-1h3.5c.6 0 1 .4 1 1 0 1.3.2 2.5.6 3.6.1.3 0 .7-.2 1z"/></svg>
        812-555-0147
      </p>
      <p class="contact-line">
        <svg viewBox="0 0 24 24"><path fill="#1e9ad6" d="M3 6h18v12H3z"/><path fill="none" stroke="#fff" stroke-width="1.6" d="M3 6l9 7 9-7M3 18l7-6M21 18l-7-6"/></svg>
        contactus@korveltait.example
      </p>
      <p class="contact-line">
        <svg viewBox="0 0 24 24"><g fill="none" stroke="#1e9ad6" stroke-width="1.6"><circle cx="12" cy="12" r="9"/><ellipse cx="12" cy="12" rx="4" ry="9"/><path d="M3 12h18M5 7h14M5 17h14"/></g></svg>
        www.korveltait.example
      </p>
    </div>
    <svg class="footer-band" viewBox="0 0 777 48" aria-hidden="true">
      <polygon points="0,26 396,26 374,48 0,48" fill="#1e9ad6"/>
      <polygon points="429,0 777,0 777,48 384,48" fill="#0a5892"/>
    </svg>
    <p class="office-hours">Office Hours: 8am-5pm EST</p>
  </section>

  <section class="card card-back">
    <div class="brand"><span class="brand-mark"></span>KORVELTA</div>
    <p class="back-url">www.korveltait.example</p>
  </section>
</body>
</html>
```